Flyer-Design für Seniorenbetreuung
Zielgruppe
Wir sind eine Genossenschaft, welche ihren Immobilienbestand gern erweitern möchte. Dafür soll für unsere Partnerfirma (welche im Seniorenbetreuungssektor tätig ist) eine Flyer erdacht werden, welcher Senioren bzw. ihre Angehörigen anspricht die Wohneigentum besitzen. Viele Senioren besitzen Ein-, Mehrfamilienhäuser oder Eigentumswohnungen und können oder wollen diese nicht weiter vererben. Zusätzlich sind sie durch die Kosten des Eigentums, wie Steuern oder Instandhaltungskosten belastet. Unsere Genossenschaft bietet eine Lösung des Problems. Eine Übernahme des Eigentums bei gleichzeitigem lebenslangem Wohnrecht. Die Zielgruppe soll in dem Flyer auf die bestehende Probleme angesprochen werden und gleichzeitig eine individuelle Lösung angeboten werden, welche eine Mitgliedschaft in dem sozialen Verbund der Genossenschaft ist.
Aufgabenstellung
Der Designer hat hier völlig freie Hand. Es sollte auf die Zielgruppe passen.
Passende Texte soll sich der Designer selbst erdenken.
Nachtrag: Ich habe mittlerweile viele Zuschriften bekommen, dass die Aufgabenstellung sich Texte auszudenken etwas zu allgemein gefasst ist, daher versuche ich hier nochmal etwas Licht in Dunkle zu bringen. Ich habe genauso wenig eine Idee, wie und mit welcher Wortwahl ein Senior auf einfühlsame Weise darauf angesprochen werden soll, ob er nicht sein Haus verkaufen möchte. Meine bisherigen Ideen waren:
'Haben sie schon einmal über den Verkauf ihrer Immobilie nachgedacht? Wussten sie, dass sie ihr Wohneigentum im vollen Umfang weiter nutzen können, ohne weiter die Kosten tragen zu müssen? Sie wollen wissen wie? Rufen sie doch einfach an und ich werde ihnen genau erklären, welche Vorzüge die Mitgliedschaft in einer Genossenschaft mit sich bringt.'
Allerdings erscheint mir das viel zu direkt und ich finde nicht die richtigen Worte diese Personengruppe in dem Maße anzusprechen, wie es nötig wäre, um sie zu einem Anruf zu bewegen. Daher hatte ich gehofft, dass sie hier ein findiger Designer findet, welcher eine bessere kreative Art hat als ich.
Vielleicht ist es die falsche Plattform, vielleicht schaffen wir es nicht die Vorgaben zu spezifizieren. Bilder anzuordnen ist sicher sehr wichtig, auch ist es wichtig aufhellende Elemente einzubringen. Aber wir suchen jemanden der einen Flyer so gestalten kann das der Flyer etwas ausdrückt, das eine Botschaft vermittelt wird, das auf einem Blick der Senior den Wunsch verspürt, bei uns anzurufen. Das heißt viel wichtiger als Bilder, ist der Inhalt der Ansprache. Nicht unbedingt der Inhalt, sondern das WIE. Nochmal: wir wollen ältere Menschen dazu bewegen ihr Eigentum auf Grund von Reperaturrückstau, Überlastung, gesundheitlichen Einschränkungen, finanziellen Schwierigkeiten, zu großem Aufwand in eine Genossenschaft einzubringen. Ds heißt S..

```html
<!DOCTYPE html>
<html lang="de">
<head>
<meta charset="utf-8">
<title>Ohne Sorgen leben – Flyer</title>
<link rel="stylesheet" href="https://fonts.googleapis.com/css2?family=Montserrat:wght@600;700;800&display=swap">
<style>
  :root {
    --canvas: #e6e6e7;
    --paper: #ffffff;
    --orange: #f5a300;
    --orange-soft: rgba(245, 163, 0, 0.88);
    --navy: #173f5f;
    --green: #1f4a33;
    --photo-warm: #d9cfc4;
    --photo-light: #eeeae6;
  }
  * { margin: 0; padding: 0; box-sizing: border-box; }
  html, body {
    width: 1200px; height: 1190px; overflow: hidden;
    background: var(--canvas);
    font-family: "Montserrat", sans-serif;
  }
  .flyer {
    position: absolute; left: 40px; top: 397px;
    width: 1120px; height: 396px;
    background: var(--paper);
    overflow: hidden;
    box-shadow: 0 6px 24px rgba(0,0,0,0.08);
  }
  .flyer__photo {
    position: absolute; left: 470px; top: 0; right: 0; bottom: 0;
    background:
      linear-gradient(90deg, var(--paper) 0%, rgba(255,255,255,0) 28%),
      radial-gradient(ellipse at 38% 55%, #8f8a86 0%, rgba(143,138,134,0) 45%),
      radial-gradient(ellipse at 66% 60%, #e7c66a 0%, rgba(231,198,106,0) 42%),
      linear-gradient(180deg, var(--photo-light) 0%, var(--photo-warm) 100%);
  }
  .flyer__headline {
    position: absolute; left: 0; top: 47px;
    width: 474px; height: 64px;
    background: var(--orange);
    color: var(--paper);
    font-weight: 800; font-size: 31px; letter-spacing: 0.5px;
    line-height: 64px; padding-left: 35px;
  }
  .flyer__question {
    position: absolute; left: 36px;
    color: var(--navy);
    font-weight: 700; font-size: 15px; line-height: 19.5px;
  }
  .flyer__question::before {
    content: ""; position: absolute; left: -36px; top: 50%;
    width: 25px; height: 3px; margin-top: -1px;
    background: var(--orange);
  }
  .flyer__question--one { top: 153px; }
  .flyer__question--two { top: 210px; }
  .flyer__call {
    position: absolute; left: 36px; top: 290px;
    color: var(--navy);
    font-weight: 700; font-size: 19.5px; line-height: 25px;
  }
  .flyer__contact {
    position: absolute; left: 653px; top: 288px;
    width: 467px; height: 72px;
    background: var(--orange-soft);
    color: var(--paper);
    padding: 14px 0 0 26px;
    font-weight: 700;
  }
  .flyer__contact-title { font-size: 17.5px; line-height: 26px; }
  .flyer__contact-phone { font-size: 15px; line-height: 22px; }
  .brand {
    position: absolute; left: 996px;
    display: flex; align-items: center; gap: 6px;
    font-weight: 700; font-size: 10px; line-height: 12px;
  }
  .brand__dot { width: 14px; height: 14px; border-radius: 50%; }
  .brand--care { top: 36px; color: var(--orange); }
  .brand--care .brand__dot { background: var(--orange); }
  .brand--coop { top: 84px; color: var(--green); }
  .brand--coop .brand__dot { background: var(--green); border-radius: 2px; }
</style>
</head>
<body>
  <main class="flyer">
    <div class="flyer__photo" role="img" aria-label="Foto: älteres Paar lächelnd auf einem Sofa in hellem Wohnzimmer, er mit Gehstock, sie in gelber Strickjacke"></div>

    <h1 class="flyer__headline">OHNE SORGEN LEBEN</h1>

    <p class="flyer__question flyer__question--one">Haben sie schon einmal über den<br>Verkauf ihrer Immobilie nachgedacht?</p>
    <p class="flyer__question flyer__question--two">Sie möchten Ihr Wohneigentum im vollen<br>Umfang weiter nutzen können, ohne weiter<br>die Kosten tragen zu müssen?</p>

    <p class="flyer__call">Dann werden Sie Mitglied in dem<br>sozialen Verbund der Genossenschaft.</p>

    <div class="flyer__contact">
      <p class="flyer__contact-title">Wir beraten Sie gerne!</p>
      <p class="flyer__contact-phone">Kontaktieren Sie uns unter: 04521 - 386 214</p>
    </div>

    <div class="brand brand--care"><span class="brand__dot"></span><span>Lindenweg<br>Seniorenbetreuung</span></div>
    <div class="brand brand--coop"><span class="brand__dot"></span><span>Hausgrund<br>Genossenschaft</span></div>
  </main>
</body>
</html>
```